Biz card, stationary for geriatric clinic
ValdoNorte Residence & Geriatric SPA
Biz card, stationary for geriatric clinic - Health
Creative Brief
Professional
Dra. Tereza Lopes Amaral
Diretora
Vale Verde - RS
tereza@valdonorte.example
www.valdonorte.example
We will need stationary i.e. letterhead, envelope, etc. For all business cards we need editable files to change for multiple employees.
Mailing address: Rua Oitenta e sete, 418. CEP 41270-000 | Bairro Jardim Vale Verde - RS

```html
<!DOCTYPE html>
<html lang="pt">
<head>
<meta charset="utf-8">
<title>ValdoNorte Residence &amp; Geriatric SPA — Stationery</title>
<link href="https://fonts.googleapis.com/css2?family=Cormorant+Garamond:wght@400;600&display=swap" rel="stylesheet">
<style>
  :root {
    --backdrop: #141414;
    --paper: #ffffff;
    --ink: #3a3a3a;
    --brand: #8a7a2e;
    --leaf: #6f8a2a;
    --gold-light: #f3e2a0;
    --gold-dark: #b98d2c;
    --faint: #ece8d8;
  }
  * { box-sizing: border-box; margin: 0; padding: 0; }
  html, body { width: 1200px; height: 643px; overflow: hidden; }
  body {
    background: var(--backdrop);
    font-family: "Cormorant Garamond", Georgia, serif;
    color: var(--ink);
    position: relative;
  }
  .sheet { position: absolute; background: var(--paper); overflow: hidden; }

  .brand { display: flex; align-items: center; gap: 6px; color: var(--brand); font-weight: 600; white-space: nowrap; }
  .brand-dot { border-radius: 50%; background: var(--leaf); flex: none; }

  /* business card front */
  .card-front { left: 48px; top: 163px; width: 240px; height: 120px; }
  .card-front .brand { position: absolute; left: 12px; top: 12px; font-size: 17px; }
  .card-front .brand-dot { width: 18px; height: 18px; }
  .card-front .details { position: absolute; left: 12px; top: 44px; width: 130px; font-size: 6.5px; line-height: 1.35; }
  .card-front .details .name { font-size: 8px; font-weight: 600; }
  .card-front .details .spacer { height: 4px; }
  .card-front .emblem { position: absolute; right: -28px; top: -6px; width: 132px; height: 132px; }

  /* business card back */
  .card-back { left: 48px; top: 334px; width: 240px; height: 122px; }
  .card-back .emblem { position: absolute; left: -30px; top: -6px; width: 134px; height: 134px; }
  .card-back .brand { position: absolute; left: 124px; top: 22px; font-size: 17px; }
  .card-back .brand-dot { width: 18px; height: 18px; }
  .card-back .address { position: absolute; left: 124px; top: 64px; width: 108px; font-size: 6px; line-height: 1.4; }

  /* letterhead */
  .letterhead { left: 324px; top: 31px; width: 408px; height: 574px; }
  .letterhead .brand { position: absolute; left: 16px; top: 30px; font-size: 28px; }
  .letterhead .brand-dot { width: 28px; height: 28px; }
  .letterhead .contact { position: absolute; left: 270px; top: 16px; font-size: 7px; line-height: 1.45; list-style: none; }
  .letterhead .contact li::before { content: "\25CF"; color: var(--brand); margin-right: 4px; font-size: 5px; vertical-align: middle; }
  .letterhead .backdrop-mark {
    position: absolute; left: 84px; top: 218px; width: 240px; height: 240px;
    border-radius: 50%; background: radial-gradient(circle, #f6f3ea 40%, var(--faint) 100%);
  }

  /* envelopes */
  .envelope-back { left: 768px; top: 139px; width: 360px; height: 168px; }
  .envelope-back svg { position: absolute; left: 0; top: 0; }
  .envelope-back .seal { position: absolute; left: 164px; top: 58px; width: 32px; height: 32px; border-radius: 50%; background: var(--leaf); }

  .envelope-front { left: 768px; top: 336px; width: 360px; height: 168px; }
  .envelope-front .brand { position: absolute; left: 52px; top: 24px; font-size: 26px; }
  .envelope-front .brand-dot { width: 26px; height: 26px; }
  .envelope-front .city { position: absolute; left: 84px; top: 62px; font-size: 9px; }
</style>
</head>
<body>

  <section class="sheet card-front" aria-label="Business card, front">
    <div class="brand"><span class="brand-dot"></span>ValdoNorte</div>
    <div class="details">
      <p class="name">Dra. Tereza Lopes Amaral</p>
      <p>Diretora</p>
      <div class="spacer"></div>
      <p>Vale Verde - RS</p>
      <div class="spacer"></div>
      <p>Fone: (051) 3000-1234</p>
      <p>Cel: (051) 9000-5678</p>
      <p>E-mail: tereza@valdonorte.example</p>
      <p>Web: www.valdonorte.example</p>
    </div>
    <svg class="emblem" viewBox="0 0 100 100" role="img" aria-label="Gold round emblem with tree and green hill illustration">
      <defs>
        <radialGradient id="goldFront" cx="40%" cy="35%" r="70%">
          <stop offset="0" stop-color="var(--gold-light)"/>
          <stop offset="1" stop-color="var(--gold-dark)"/>
        </radialGradient>
      </defs>
      <circle cx="50" cy="50" r="50" fill="url(#goldFront)"/>
      <circle cx="50" cy="50" r="42" fill="#e9e5c4"/>
    </svg>
  </section>

  <section class="sheet card-back" aria-label="Business card, back">
    <svg class="emblem" viewBox="0 0 100 100" role="img" aria-label="Gold round emblem with tree and green hill illustration">
      <defs>
        <radialGradient id="goldBack" cx="60%" cy="35%" r="70%">
          <stop offset="0" stop-color="var(--gold-light)"/>
          <stop offset="1" stop-color="var(--gold-dark)"/>
        </radialGradient>
      </defs>
      <circle cx="50" cy="50" r="50" fill="url(#goldBack)"/>
      <circle cx="50" cy="50" r="42" fill="#e6e3bf"/>
    </svg>
    <div class="brand"><span class="brand-dot"></span>ValdoNorte</div>
    <p class="address">Rua Oitenta e sete, 418. CEP 41270-000 | Bairro Jardim Vale Verde - RS</p>
  </section>

  <section class="sheet letterhead" aria-label="Letterhead">
    <div class="brand"><span class="brand-dot"></span>ValdoNorte</div>
    <ul class="contact">
      <li>(051) 3000-1234</li>
      <li>(051) 9000-5678</li>
      <li>tereza@valdonorte.example</li>
      <li>www.valdonorte.example</li>
      <li>Vale Verde - RS</li>
    </ul>
    <div class="backdrop-mark"></div>
  </section>

  <section class="sheet envelope-back" aria-label="Envelope, back">
    <svg width="360" height="168" viewBox="0 0 360 168" aria-hidden="true">
      <polyline points="0,0 0,30 180,74 360,30 360,0" fill="none" stroke="#d8d8d8" stroke-width="1"/>
    </svg>
    <div class="seal"></div>
  </section>

  <section class="sheet envelope-front" aria-label="Envelope, front">
    <div class="brand"><span class="brand-dot"></span>ValdoNorte</div>
    <p class="city">Vale Verde - RS</p>
  </section>

</body>
</html>
```